When the boots match march on! book cover design

Book cover for a business, non-fiction book.
About stepping up, being who you truly are, and willing not to fit in.

TITLE: When The Boots Match, March On!
SUBTITLE: Quit copying the chief others expect of you and begin shaping the chief nobody else could ever shape...
AUTHOR: Tobias Hartwell-Brenner
Updates

we never uploaded the brief

Target Market(s)

Business people, curious leaders, insiders who have a secret itch to be an outsider
AGE: 35-50 years old

Font styles to use
Sans Serif
Other font styles liked:
• designer's choice!

Requirements
Must have
• Very visual
Imagery must reflect the topic of the book

```html
<!DOCTYPE html>
<html lang="en">
<head>
<meta charset="utf-8">
<title>When The Boots Match, March On! — Book Cover</title>
<link rel="stylesheet" href="https://fonts.googleapis.com/css2?family=Bebas+Neue&family=Montserrat:wght@500;600&family=Gochi+Hand&display=swap">
<style>
  :root {
    --backdrop: #e6e6e6;
    --strip: #b9f0ef;
    --panel-top: #10d0e6;
    --panel-bottom: #0599bd;
    --ink: #141414;
    --accent: #d4141c;
    --paper: #ffffff;
    --art-red: #c8101a;
    --art-blue: #1a8fb0;
  }
  * { box-sizing: border-box; margin: 0; padding: 0; }
  html, body { width: 1200px; height: 800px; overflow: hidden; }
  body {
    background: var(--backdrop);
    display: flex;
    align-items: center;
    justify-content: center;
  }
  .cover {
    position: relative;
    width: 480px;
    height: 740px;
    background: linear-gradient(90deg, var(--strip) 0 168px, transparent 168px),
                linear-gradient(160deg, var(--panel-top), var(--panel-bottom));
    overflow: hidden;
  }
  .cover-art {
    position: absolute;
    left: 14px;
    top: 90px;
    width: 440px;
    height: 210px;
  }
  .subtitle {
    position: absolute;
    left: 12px;
    top: 450px;
    width: 146px;
    text-align: right;
    font-family: "Montserrat", sans-serif;
    font-weight: 500;
    font-size: 14.5px;
    line-height: 1.45;
    text-transform: uppercase;
    color: var(--ink);
  }
  .subtitle .highlight { color: var(--accent); font-weight: 600; }
  .title {
    position: absolute;
    left: 168px;
    right: 0;
    top: 355px;
    text-align: center;
    font-family: "Bebas Neue", sans-serif;
    font-size: 80px;
    line-height: 0.98;
    color: var(--paper);
    letter-spacing: 0.5px;
  }
  .author {
    position: absolute;
    left: 168px;
    right: 0;
    bottom: 26px;
    text-align: center;
    font-family: "Gochi Hand", cursive;
    font-size: 27px;
    color: var(--ink);
  }
</style>
</head>
<body>
  <main class="cover">
    <svg class="cover-art" viewBox="0 0 440 210" role="img" aria-label="Illustration: a caped businessman with a briefcase flying out through a shattered wall">
      <defs>
        <linearGradient id="art-fill" x1="0" x2="1" y1="0" y2="0">
          <stop offset="0" stop-color="var(--art-blue)"/>
          <stop offset="0.35" stop-color="var(--art-red)"/>
          <stop offset="1" stop-color="var(--art-red)" stop-opacity="0"/>
        </linearGradient>
      </defs>
      <rect x="0" y="0" width="440" height="210" rx="12" fill="url(#art-fill)" opacity="0.55"/>
    </svg>

    <p class="subtitle">
      Quit copying<br>the chief<br>others expect<br>of you and<br>
      <span class="highlight">begin shaping<br>the chief<br>nobody else<br>could ever<br>shape</span>
    </p>

    <h1 class="title">When<br>The Boots<br>Match,<br>March On!</h1>

    <p class="author">Tobias Hartwell-Brenner</p>
  </main>
</body>
</html>
```